Marcus Lindqvist Photography needs a business card designs

I am looking for a business card with a logo clean and simple which I can use that logo on my website or on my pictures. It has to be very classy and very professional. Please look at my website at www.marcuslvqphoto.com for my signature. I'm thinking of something like that for my signature/logo. I'm still working on my website but you get an idea. I'm open to any design but not too busy graphics.

I will be printing the business card from qrivel.com.

Surprise me :)

contact me if you have any questions.

-ML

I'm receiving a lot of black background at the moment. I know my website is all black doesn't mean I want my card to be all black. Please send in with some white background as well. Thanks :)

check out some business cards that I found online. I think they are simple and look really awesome. I don't want a card that is too busy.

http://www.marcuslvqphoto.com/p270092084

Reason: Please extend the date for me. I haven't really receive any good design yet.

Printing

• -a logo that related to my first and last initial of my name "ML"
-double sided
• -I don't want my background to be all black.
-no pictures on the card

```html
<!DOCTYPE html>
<html lang="en">
<head>
<meta charset="utf-8">
<title>Marcus Lindqvist Photography – Business Card</title>
<link rel="stylesheet" href="https://fonts.googleapis.com/css2?family=Tenor+Sans&family=EB+Garamond:wght@400;500&display=swap">
<style>
  :root {
    --backdrop: #e6e6e2;
    --card: #fbfaf6;
    --ink: #4a4a48;
    --ink-soft: #6d6d6a;
    --accent: #b3161c;
    --accent-deep: #9e1217;
  }
  * { margin: 0; padding: 0; box-sizing: border-box; }
  html, body {
    width: 1200px;
    height: 788px;
    overflow: hidden;
    background: var(--backdrop);
  }
  .stage {
    position: relative;
    width: 1200px;
    height: 788px;
    display: flex;
    justify-content: center;
    align-items: center;
    gap: 80px;
  }
  .card {
    position: relative;
    width: 340px;
    height: 596px;
    background: var(--card);
    border-radius: 24px;
    overflow: hidden;
    box-shadow: 0 10px 28px rgba(0, 0, 0, 0.12), 0 2px 6px rgba(0, 0, 0, 0.08);
    font-family: "Tenor Sans", "Helvetica Neue", sans-serif;
  }

  /* Monogram set as text */
  .monogram {
    color: var(--accent);
    font-family: "Tenor Sans", "Helvetica Neue", sans-serif;
    font-size: 44px;
    letter-spacing: 4px;
    line-height: 1;
  }

  .wordmark {
    font-variant: small-caps;
    line-height: 1.05;
  }
  .wordmark .first { color: var(--ink); }
  .wordmark .last { color: var(--accent); }
  .wordmark .trade {
    display: block;
    color: var(--ink-soft);
    font-size: 13px;
    letter-spacing: 2px;
  }

  /* Back side */
  .card-back .monogram {
    position: absolute;
    top: 70px;
    left: 48px;
  }
  .card-back .wordmark {
    position: absolute;
    top: 150px;
    left: 48px;
    font-size: 24px;
  }
  .card-back .wordmark .first,
  .card-back .wordmark .last { display: block; }
  .card-back .wordmark .last { padding-left: 22px; }
  .card-back .wordmark .trade { padding-left: 40px; margin-top: 2px; }

  .contact {
    position: absolute;
    right: 30px;
    bottom: 40px;
    transform-origin: right bottom;
    transform: rotate(-90deg) translateX(100%);
    font-family: "EB Garamond", Georgia, serif;
    font-size: 14px;
    line-height: 1.35;
    color: var(--ink);
    white-space: nowrap;
  }
  .contact .email { color: var(--accent); }

  /* Front side */
  .card-front .monogram {
    position: absolute;
    top: 196px;
    left: 0;
    right: 0;
    text-align: center;
    font-size: 52px;
  }
  .card-front .wordmark {
    position: absolute;
    top: 272px;
    left: 0;
    right: 0;
    text-align: center;
    font-size: 23px;
  }
  .card-front .wordmark .trade { margin-top: 2px; }

  .skyline {
    position: absolute;
    left: 0;
    right: 0;
    bottom: 0;
    height: 110px;
    background: linear-gradient(to bottom, rgba(179, 22, 28, 0) 0%, var(--accent) 22%, var(--accent-deep) 100%);
  }
</style>
</head>
<body>
  <main class="stage">
    <section class="card card-back" aria-label="Card back">
      <div class="monogram">ML</div>
      <h1 class="wordmark">
        <span class="first">Marcus</span>
        <span class="last">Lindqvist</span>
        <span class="trade">Photography</span>
      </h1>
      <address class="contact">
        48 Harbour Lane<br>
        NSW 2000 Australia<br>
        0391 204 775<br>
        <span class="email">info@marcuslvqphoto.com</span>
      </address>
    </section>

    <section class="card card-front" aria-label="Card front">
      <div class="monogram">ML</div>
      <h2 class="wordmark">
        <span class="first">Marcus</span> <span class="last">Lindqvist</span>
        <span class="trade">Photography</span>
      </h2>
      <div class="skyline" role="img" aria-label="Red city skyline silhouette with domes and towers along the bottom edge"></div>
    </section>
  </main>
</body>
</html>
```